Petal Crate Guild - A Monthly Subscription for Essential Oils - Storevane Website Design

A monthly subscription company. Need a Storevane Website Design and uploaded to fully work with Brisk Renewals.

Please look at these sites for examples as well as the images I enclosed.

https://purelymeadow.com/
https://www.florant-xa.com/
https://www.dinnertrove.com/
https://www.globalsnackora.com/

```html
<!DOCTYPE html>
<html lang="en">
<head>
<meta charset="utf-8">
<title>Petal Crate Guild — Monthly Essential Oils</title>
<link rel="stylesheet" href="https://fonts.googleapis.com/css2?family=Open+Sans:wght@400;600&family=Playfair+Display:wght@400;700&display=swap">
<style>
:root{
  --accent:#e8400c;
  --ink:#222222;
  --body:#444444;
  --panel:#e8e8e8;
  --dark:#2b2b2b;
  --footer:#232323;
  --white:#ffffff;
  --muted:#9a9a9a;
}
*{margin:0;padding:0;box-sizing:border-box}
html,body{width:1200px;height:4228px;overflow:hidden}
body{position:relative;background:var(--white);font-family:"Open Sans",Arial,sans-serif;color:var(--body)}
.abs{position:absolute}
.serif{font-family:"Playfair Display",Georgia,serif}
.rule{position:absolute;height:6px;background:var(--accent)}
.btn-accent{position:absolute;background:var(--accent);color:var(--white);font-size:16px;font-weight:600;display:flex;align-items:center;justify-content:center;letter-spacing:.2px}
.btn-outline{position:absolute;border:2px solid var(--ink);color:var(--ink);font-size:14px;display:flex;align-items:center;justify-content:center}

/* hero */
.hero{left:0;top:0;width:1200px;height:614px;background:linear-gradient(135deg,#3b4a5a 0%,#4a3a2a 35%,#5a4530 60%,#2e2418 100%)}
.hero-shade{left:0;top:0;width:1200px;height:614px;background:rgba(0,0,0,.35)}
.brand{left:0;top:22px;width:1200px;text-align:center;color:var(--white);font-size:33px;font-weight:700}
.hero-title{left:0;top:250px;width:1200px;text-align:center;color:var(--white);font-size:68px;font-weight:400}
.inside-link{left:143px;top:539px;color:var(--white);font-size:20px;text-decoration:underline}

/* intro */
.intro-photo{left:123px;top:772px;width:361px;height:311px;background:radial-gradient(ellipse at 50% 50%,#5f8a4a 0%,#c9d3c1 45%,#ffffff 72%)}
.intro-panel{left:600px;top:614px;width:600px;height:615px;background:var(--panel)}
.h2{font-size:34px;font-weight:700;color:var(--ink);line-height:41px}
.copy{font-size:15px;line-height:27.5px;color:var(--body)}

/* video */
.video{left:0;top:1229px;width:1200px;height:614px;background:linear-gradient(90deg,#3a2a1e 0%,#6b4a2a 30%,#4b3624 55%,#7a5a3a 80%,#3a2a20 100%)}
.video-shade{left:0;top:1229px;width:1200px;height:614px;background:linear-gradient(180deg,rgba(0,0,0,.15),rgba(120,100,110,.25))}

/* collections */
.tile{top:2052px;width:400px;height:399px;display:flex;align-items:center;justify-content:center;color:var(--white);font-size:24px;letter-spacing:.5px}
.tile-1{left:0;background:linear-gradient(160deg,#d9cfd2 0%,#b98a92 50%,#5e3a30 100%)}
.tile-2{left:400px;width:400px;background:linear-gradient(160deg,#3a2a38 0%,#6a4a6e 50%,#2e2430 100%)}
.tile-3{left:800px;background:linear-gradient(160deg,#4a3a3c 0%,#8a5a6a 50%,#3a2a2c 100%)}
.tile span{text-shadow:0 1px 3px rgba(0,0,0,.35)}

/* feature */
.feature{left:0;top:2451px;width:1200px;height:432px;background:radial-gradient(ellipse at 75% 45%,#ffffff 0%,#f2f2f2 40%,#e4e4e4 100%)}
.feature-photo{left:771px;top:2528px;width:247px;height:279px;background:linear-gradient(180deg,#f4f4f4,#dcdcdc)}

/* product */
.product-photo{left:144px;top:2965px;width:432px;height:430px;background:linear-gradient(135deg,#4d5e6c 0%,#2a2a2e 40%,#1c1c20 70%,#5a6a78 100%)}
.select{left:624px;top:3074px;width:431px;height:65px;background:#ececec;color:#555;font-size:18px;padding-left:30px;display:flex;align-items:center}
.btn-cart{left:624px;top:3180px;width:431px;height:62px;border:2px solid var(--ink);color:var(--ink);font-size:18px;display:flex;align-items:center;justify-content:center}
.btn-sub{left:624px;top:3260px;width:431px;height:62px;background:var(--dark);color:var(--white);font-size:18px;display:flex;align-items:center;justify-content:center}
.details{left:624px;top:3356px;width:431px;display:flex;justify-content:center;align-items:center;gap:8px;font-size:15px;color:#555}

/* cta */
.cta{left:0;top:3468px;width:1200px;height:480px;background:linear-gradient(150deg,#3a3026 0%,#2a2620 45%,#4a3a2a 75%,#2a241e 100%)}
.cta-shade{left:0;top:3468px;width:1200px;height:480px;background:rgba(0,0,0,.3)}

/* footer */
.footer{left:0;top:3948px;width:1200px;height:280px;background:var(--footer)}
.foot-link{left:144px;font-size:13px;color:#bdbdbd;letter-spacing:.3px}
.card{position:absolute;top:4152px;width:30px;height:18px;border-radius:2px}
</style>
</head>
<body>

<!-- hero -->
<div class="abs hero" role="img" aria-label="Hands opening a wooden crate of essential oil bottles"></div>
<div class="abs hero-shade"></div>
<svg class="abs" style="left:145px;top:37px" width="27" height="23" viewBox="0 0 27 23" aria-label="Menu">
  <rect y="0" width="27" height="4" fill="#fff"/><rect y="9.5" width="27" height="4" fill="#fff"/><rect y="19" width="27" height="4" fill="#fff"/>
</svg>
<div class="abs brand serif">Petal Crate Guild</div>
<svg class="abs" style="left:1026px;top:35px" width="28" height="26" viewBox="0 0 28 26" aria-label="Cart">
  <path d="M0 2h5l4 14h15l3-10H8" fill="none" stroke="#fff" stroke-width="3"/>
  <rect x="8" y="5" width="18" height="9" fill="#fff"/>
  <circle cx="11" cy="22" r="2.6" fill="#fff"/><circle cx="22" cy="22" r="2.6" fill="#fff"/>
</svg>
<h1 class="abs hero-title serif">Aliquam erat volutpat</h1>
<div class="btn-accent" style="left:515px;top:358px;width:168px;height:42px">SUBSCRIBE NOW</div>
<div class="abs inside-link">INSIDE BOX</div>

<!-- intro -->
<div class="abs intro-photo" role="img" aria-label="Open gift box with herbs, candle, dried orange and oil bottle"></div>
<div class="abs intro-panel"></div>
<div class="rule" style="left:704px;top:750px;width:135px"></div>
<h2 class="abs h2 serif" style="left:704px;top:776px;width:400px">Pellentesque blandit lacus eget nunc</h2>
<p class="abs copy" style="left:704px;top:871px;width:360px">Phasellus consequat sagittis nisi suscipit feugiat. Cras eget leo sed nunc hendrerit ultricies eu at nisl. Praesent iaculis faucibus urna sit amet lacinia. Maecenas consequat justo enim, ac mattis massa imperdiet quis. Fusce eget neque elit. Sed augue orci, elementum in magna congue.</p>
<div class="btn-outline" style="left:704px;top:1051px;width:120px;height:42px">VIEW MORE</div>

<!-- video -->
<div class="abs video" role="img" aria-label="Amber oil bottles beside dried lavender"></div>
<div class="abs video-shade"></div>
<svg class="abs" style="left:567px;top:1505px" width="64" height="64" viewBox="0 0 64 64" aria-label="Play video">
  <circle cx="32" cy="32" r="30" fill="none" stroke="#fff" stroke-width="2.5"/>
  <path d="M26 20v24l18-12z" fill="none" stroke="#fff" stroke-width="2.5" stroke-linejoin="round"/>
</svg>

<!-- collections heading -->
<div class="rule" style="left:532px;top:1923px;width:136px"></div>
<h2 class="abs serif" style="left:0;top:1948px;width:1200px;text-align:center;font-size:34px;font-weight:700;color:var(--ink)">Aliquam consectetur molestie</h2>
<p class="abs" style="left:0;top:2001px;width:1200px;text-align:center;font-size:15px;color:var(--body)">Fusce sollicitudin lorem et luctus volutpat. Proin placerat dapibus gravida. In tristique tristique nulla eget hendrerit.</p>

<div class="abs tile tile-1" role="img" aria-label="Oil bottles with tea light and pink petals"><span>NULLA FACILISI</span></div>
<div class="abs tile tile-2" role="img" aria-label="Purple candles and glass oil bottle"><span>ETIAM MASSA</span></div>
<div class="abs tile tile-3" role="img" aria-label="Amber bottle among falling rose petals"><span>ALIQUAM ERAT</span></div>

<!-- feature -->
<div class="abs feature"></div>
<div class="rule" style="left:144px;top:2553px;width:135px"></div>
<h2 class="abs h2 serif" style="left:144px;top:2578px">Etiam imperdiet lectus</h2>
<p class="abs copy" style="left:144px;top:2632px;width:340px">Vivamus lacus justo, ultrices nec erat in, euismod iaculis mauris. Vivamus eleifend vitae nulla vel malesuada. In ac malesuada lacus.</p>
<div class="btn-outline" style="left:144px;top:2738px;width:119px;height:44px">VIEW MORE</div>
<div class="abs feature-photo" role="img" aria-label="White dropper bottle beside its white box"></div>

<!-- product -->
<div class="abs product-photo" role="img" aria-label="Wooden box filled with rows of essential oil bottles"></div>
<h3 class="abs serif" style="left:624px;top:2975px;width:440px;text-align:center;font-size:33px;font-weight:400;color:var(--ink)">Maecenas</h3>
<div class="abs serif" style="left:624px;top:3028px;width:440px;text-align:center;font-size:19px;color:var(--ink)">$200.00</div>
<div class="abs select">Number of Oils Bottles
  <svg style="position:absolute;right:20px;top:27px" width="18" height="10" viewBox="0 0 18 10"><path d="M0 0h18L9 10z" fill="#555"/></svg>
</div>
<div class="abs btn-cart">ADD TO CART</div>
<div class="abs btn-sub">SUBSCRIBE NOW</div>
<div class="abs details">
  <svg width="20" height="16" viewBox="0 0 20 16"><g fill="#444"><rect width="3" height="3"/><rect x="5" width="15" height="3"/><rect y="6.5" width="3" height="3"/><rect x="5" y="6.5" width="15" height="3"/><rect y="13" width="3" height="3"/><rect x="5" y="13" width="15" height="3"/></g></svg>
  FULL DETAILS
</div>

<!-- cta -->
<div class="abs cta" role="img" aria-label="Close-up of oil bottles in a wooden crate"></div>
<div class="abs cta-shade"></div>
<h2 class="abs serif" style="left:0;top:3595px;width:1200px;text-align:center;font-size:68px;font-weight:400;color:var(--white)">Fusce vitae lectus sit</h2>
<p class="abs" style="left:0;top:3696px;width:1200px;text-align:center;font-size:22px;color:var(--white)">Aenean placerat, nibh vel accumsan aliquet, magna</p>
<div class="btn-accent" style="left:515px;top:3754px;width:168px;height:46px">SUBSCRIBE NOW</div>

<!-- footer -->
<div class="abs footer"></div>
<div class="abs foot-link" style="top:3991px">SEARCH</div>
<div class="abs foot-link" style="top:4023px">ARTICLES</div>
<div class="abs foot-link" style="top:4055px">FAQS</div>
<div class="abs foot-link" style="top:4087px">CONTACT US</div>

<div class="abs" style="left:734px;top:3990px;font-size:15px;color:#d0d0d0">SIGN UP FOR UPDATES</div>
<div class="abs" style="left:734px;top:4023px;font-size:11px;color:#bdbdbd">Fusce vitae lectus sit amet mi pulvinar maximus</div>
<div class="abs" style="left:747px;top:4074px;font-size:10px;color:var(--muted)">Email Address</div>
<div class="abs" style="left:987px;top:4074px;font-size:10px;color:#bdbdbd">SUBSCRIBE ›</div>
<div class="abs" style="left:734px;top:4096px;width:321px;height:2px;background:#888"></div>

<div class="abs" style="left:0;top:4154px;width:1200px;text-align:center;font-size:11px;color:#bdbdbd;padding-right:0">Copyright © 2020 Petal Crate Guild. All rights reserved.</div>

<div class="card" style="left:840px;background:#f2f2f2"></div>
<div class="card" style="left:879px;background:#f2f2f2"></div>
<div class="card" style="left:918px;background:#3b7bc4"></div>
<div class="card" style="left:957px;background:#f2f2f2"></div>
<div class="card" style="left:996px;background:#f2f2f2"></div>
<div class="card" style="left:1025px;background:#f2f2f2"></div>

</body>
</html>
```